Business Card - Self Employed Director

My husband needs a business card design. 2 sided printing required.

He is self employed, in the vineyard management and renewable energy sectors (see below for more information) and design and accent colors should reflect this.

Design should be modern but classic and professional too.

Card to show personal contact information only. Exact information subject to confirmation on finalizing design as we are moving soon and need to confirm the exact details.

Dorian Fellowes
email: dorian.fellowes@quillbarrow.example
mobile: 021 048 53117
home: +64 (0) 3 6142 875
184 Corbin Ridge Rise, RD4 Fenwold, Tarrow Vale, NZ 7390

I like the attached design by Pik for inspiration.

The reverse side should show name in bottom right corner with the pattern possibly reflecting renewable energy? Waves? Wind? Sea green, teal? Fresh, clean
Image on reverse should not be a photograph but a clean graphic based print on white background. Sans serfic fonts, Charcoal grey not black with accent colors reflected on the back?

Print ready artwork will be required. Please ask any questions :-) THANKS

Printing

Font styles to use
Sans Serif

Colors
86cfc6
ffffff
85abd2

Requirements
Must have
• Contact information as show
Should not have
• Anything cute, no red. No fancy flourish fonts.

```html
<!DOCTYPE html>
<html lang="en">
<head>
<meta charset="utf-8">
<title>Dorian Fellowes — Business Card</title>
<link rel="stylesheet" href="https://fonts.googleapis.com/css2?family=Fira+Sans:wght@400;600&display=swap">
<style>
  :root {
    --charcoal: #4a4c4e;
    --teal: #5fb8b8;
    --sea: #86cfc6;
    --sky: #85abd2;
    --paper: #ffffff;
    --backdrop: #e9eaeb;
  }
  * { box-sizing: border-box; margin: 0; padding: 0; }
  html, body {
    width: 1200px; height: 1000px; overflow: hidden;
    background: var(--backdrop);
    font-family: "Fira Sans", Arial, sans-serif;
  }
  .sheet {
    position: relative; width: 1200px; height: 1000px;
    display: flex; flex-direction: column; align-items: center;
    justify-content: center; gap: 60px;
  }
  .card {
    position: relative; width: 700px; height: 400px;
    background: var(--paper);
    box-shadow: 0 2px 10px rgba(0,0,0,0.08);
    overflow: hidden;
  }
  /* Front */
  .card-front .corner-tiles {
    position: absolute; top: 0; right: 0; width: 230px; height: 130px;
  }
  .contact-block {
    position: absolute; left: 80px; top: 170px; color: var(--charcoal);
  }
  .holder-name {
    font-weight: 600; font-size: 38px; letter-spacing: 0.2px;
    margin-bottom: 14px;
  }
  .contact-list { list-style: none; font-size: 20px; line-height: 28px; }
  .contact-list li { display: flex; align-items: center; gap: 10px; }
  .contact-list svg { width: 16px; height: 16px; flex: none; }
  .address { margin-top: 16px; font-size: 20px; line-height: 26px; }
  /* Back */
  .card-back .pattern-field { position: absolute; inset: 0; }
  .card-back .holder-name {
    position: absolute; right: 40px; bottom: 30px; margin: 0;
    font-size: 34px; color: var(--charcoal);
  }
</style>
</head>
<body>
<main class="sheet">
  <section class="card card-front" aria-label="Business card front">
    <svg class="corner-tiles" viewBox="0 0 230 130" role="img" aria-label="Cluster of teal and blue square tiles">
      <defs>
        <linearGradient id="tileCorner" x1="0" y1="1" x2="1" y2="0">
          <stop offset="0" stop-color="#85abd2" stop-opacity="0.15"/>
          <stop offset="0.5" stop-color="#86cfc6" stop-opacity="0.75"/>
          <stop offset="1" stop-color="#5fb8b8"/>
        </linearGradient>
      </defs>
      <polygon points="230,0 230,95 150,130 90,90 40,70 60,20 130,0" fill="url(#tileCorner)"/>
    </svg>
    <div class="contact-block">
      <h1 class="holder-name">Dorian Fellowes</h1>
      <ul class="contact-list">
        <li>
          <svg viewBox="0 0 16 16" aria-hidden="true"><path d="M3 1.5l3 .5 1 3-2 1.5c1 2 2.5 3.5 4.5 4.5L11 9l3 1 .5 3c-1 1.5-3 2-4.5 1.5C6 13 3 10 1.5 6 1 4.5 1.5 2.5 3 1.5z" fill="var(--teal)"/></svg>
          <span>+64 (0) 3 6142 875</span>
        </li>
        <li>
          <svg viewBox="0 0 16 16" aria-hidden="true"><rect x="4" y="1" width="8" height="14" rx="1.5" fill="var(--teal)"/><rect x="5.5" y="3" width="5" height="8" fill="#fff"/><circle cx="8" cy="13" r="0.9" fill="#fff"/></svg>
          <span>021 048 53117</span>
        </li>
        <li>
          <svg viewBox="0 0 16 16" aria-hidden="true"><rect x="1" y="3" width="14" height="10" rx="1" fill="var(--teal)"/><path d="M1.5 3.5L8 9l6.5-5.5" stroke="#fff" stroke-width="1.3" fill="none"/></svg>
          <span>dorian.fellowes@quillbarrow.example</span>
        </li>
      </ul>
      <p class="address">184 Corbin Ridge Rise<br>RD4 Fenwold, Tarrow Vale, NZ 7390</p>
    </div>
  </section>

  <section class="card card-back" aria-label="Business card back">
    <svg class="pattern-field" viewBox="0 0 700 400" role="img" aria-label="Mosaic of soft teal and blue square tiles spreading from the upper right">
      <defs>
        <linearGradient id="tileField" x1="0" y1="1" x2="1" y2="0">
          <stop offset="0" stop-color="#85abd2" stop-opacity="0.35"/>
          <stop offset="0.45" stop-color="#6fb6c6" stop-opacity="0.8"/>
          <stop offset="0.8" stop-color="#86cfc6" stop-opacity="0.7"/>
          <stop offset="1" stop-color="#86cfc6" stop-opacity="0.25"/>
        </linearGradient>
      </defs>
      <polygon points="0,130 180,90 330,30 520,0 700,0 700,150 560,200 470,300 330,330 180,400 0,400" fill="url(#tileField)"/>
    </svg>
    <p class="holder-name">Dorian Fellowes</p>
  </section>
</main>
</body>
</html>
```